Billboard design - consider what a billboard is

Design a billboard using my logo - Billboard is 6m x 3m
A Billboard is advertising for my company that is on a big sign.

Has to be clean and easy to read, and ideally highlights that we are Residential and Commercial builders.

Keep it clean and easy to read

The contact number for the board is

022 583 7092
www.harbourframeworks.co.nz
info@harbourframeworks.co.nz

Doesnt have to have all contact details if it doesnt fit

Has to catch peoples attention to contact us if they need a builder

Can you please change the sign to be all white writing, with black background ?
Updates

Please consider what a billboard is...

The design needs to be suitable for a billboard..

Target Market(s)

people driving past

Industry/Entity Type

Construction

Logo Text

Wellington Builder, website email address, contact number

Colors
0054AA
0677BA
7BADD7
CADEEF
E8F1F8

Requirements
Must have
• Easy to read
Nice to have
• easy to read, can clearly see contact details

```html
<!DOCTYPE html>
<html lang="en">
<head>
<meta charset="utf-8">
<title>Harbour Frameworks Billboard</title>
<link href="https://fonts.googleapis.com/css2?family=Arimo:wght@700&family=Raleway:wght@400;500&display=swap" rel="stylesheet">
<style>
  :root {
    --brand-blue: #5a8bc7;
    --brand-grey: #6d6664;
    --paper: #ffffff;
  }
  html, body {
    margin: 0;
    padding: 0;
    overflow: hidden;
    background: var(--paper);
  }
  .billboard {
    position: relative;
    width: 1200px;
    height: 600px;
    background: var(--paper);
    overflow: hidden;
  }
  .sector-banner {
    position: absolute;
    top: 0;
    left: 0;
    width: 1200px;
    height: 160px;
  }
  .sector-banner__label {
    position: absolute;
    left: 880px;
    top: 50px;
    width: 300px;
    margin: 0;
    text-align: center;
    font-family: "Raleway", sans-serif;
    font-weight: 500;
    font-size: 22px;
    line-height: 33px;
    letter-spacing: 0.5em;
    color: var(--paper);
  }
  .brand {
    position: absolute;
    left: 245px;
    top: 185px;
    display: flex;
    align-items: center;
    gap: 28px;
  }
  .brand__mark {
    width: 66px;
    height: 66px;
    background: var(--brand-grey);
    flex: none;
  }
  .brand__name {
    margin: 0;
    font-family: "Arimo", sans-serif;
    font-weight: 700;
    font-size: 92px;
    line-height: 96px;
    color: var(--brand-blue);
  }
  .phone {
    position: absolute;
    left: 0;
    top: 458px;
    width: 1200px;
    margin: 0;
    text-align: center;
    font-family: "Arimo", sans-serif;
    font-weight: 700;
    font-size: 48px;
    line-height: 60px;
    letter-spacing: 0.35em;
    color: var(--brand-blue);
  }
  .divider {
    position: absolute;
    left: 125px;
    top: 523px;
    width: 947px;
    height: 4px;
    background: var(--brand-grey);
  }
  .website {
    position: absolute;
    left: 0;
    top: 539px;
    width: 1200px;
    margin: 0;
    text-align: center;
    font-family: "Raleway", sans-serif;
    font-weight: 400;
    font-size: 34px;
    line-height: 44px;
    letter-spacing: 0.62em;
    text-indent: 0.62em;
    color: var(--brand-blue);
  }
</style>
</head>
<body>
  <main class="billboard">
    <svg class="sector-banner" viewBox="0 0 1200 160" aria-hidden="true">
      <polygon points="852,126 1200,126 1200,147 843,147" fill="var(--brand-grey)"/>
      <polygon points="866,35 1200,35 1200,126 827,126" fill="var(--brand-blue)"/>
    </svg>
    <p class="sector-banner__label">COMMERCIAL &amp;<br>RESIDENTIAL</p>

    <div class="brand">
      <span class="brand__mark"></span>
      <h1 class="brand__name">Harbour<br>Frameworks</h1>
    </div>

    <p class="phone">022 583 7092</p>
    <div class="divider"></div>
    <p class="website">HARBOURFRAMEWORKS.CO.NZ</p>
  </main>
</body>
</html>
```